KRV Holdfast Manufacturer New Web Design

We need a new theme designed for metal fastener manufacturing company, KRV Holdfast Group, a $60M division of Benmore Forge Holdings, Inc. We manufacture screw, pins and washers to industrial customers (non-Automotive) such as Tallow Appliance, Marcus Fenwold, BRU, Veltrin, etc. Our current website is www.holdfastparts.example. We would like to stick with the same logo/color scheme, however, I'm aiming to modernize the website's look and feel.

Here are some of our competitor's websites:
- https://www.torvanix.example/
- http://quellbrook.example/
- http://www.morrowbuiltcouplingworks.example/
- http://pegsandoddments.example/
- http://www.dunmerebolting.example/

Target Market(s)

We primarily want to target engineers working in the following markets:
- Appliance (Tallow Appliance, Kelvanor)
- Ag (Fenwold, BRU)
- Recreational Vehicle (Veltrin, Briar Fox)
- Outdoor Power (Oldmeadow, Vexa)

We secondarily want to target buyers working at the above markets as well as buyers at Fastener distributors such as Boltrin, Provision Dynamics, Hollis Parfet.

Industry/Entity Type

Metal Forging

Number of Pages Required

1 page

Requirements
Must have
• For products: "Threaded" product as the primary focus. "Pins" product is the secondary focus, followed by all others.
• Please use same logo and color scheme as I do not plan to change.
Nice to have
• Highlight our featured proprietary products (pamphlets attached). KRV Holdfast's KIN-V, LumDrive, Holdfast Spiral, Pelmont.

```html
<!DOCTYPE html>
<html lang="en">
<head>
<meta charset="utf-8">
<title>KRV Holdfast Group</title>
<link href="https://fonts.googleapis.com/css2?family=Open+Sans:wght@400;600;700&display=swap" rel="stylesheet">
<style>
:root{
  --blue:#2f80c2;
  --nav:#3a87c7;
  --title:#2b7dbd;
  --teal:#17a58a;
  --teal-light:#3dd3b0;
  --dark:#1b1f27;
  --ink:#2a2a2a;
  --muted:#8a8a8a;
  --band:#ececec;
  --white:#fff;
}
*{margin:0;padding:0;box-sizing:border-box}
html,body{width:698px;height:1200px;overflow:hidden}
body{font-family:"Open Sans",sans-serif;color:var(--ink);background:var(--white);position:relative}

/* header */
.site-header{position:absolute;top:0;left:0;width:698px;height:38px}
.brand{position:absolute;left:50px;top:6px;display:flex;align-items:center;gap:6px}
.brand-dot{width:26px;height:26px;border-radius:50%;background:var(--blue)}
.brand-name{font-size:14px;font-weight:600;color:var(--blue);white-space:nowrap}
.header-contacts{position:absolute;right:50px;top:14px;display:flex;gap:18px;font-size:8px;color:#333}
.header-contacts span{display:flex;align-items:center;gap:4px}
.header-contacts svg{width:8px;height:8px;fill:#333}

.main-nav{position:absolute;top:38px;left:0;width:698px;height:21px;background:var(--nav);display:flex;justify-content:center}
.main-nav a{color:var(--white);font-size:8px;font-weight:600;text-decoration:none;line-height:21px;padding:0 15px}

/* hero */
.hero{position:absolute;top:59px;left:0;width:698px;height:241px;background:var(--dark)}
.hero-photo{position:absolute;left:0;top:0;width:340px;height:241px;background:linear-gradient(110deg,#2b2e35 0%,#6f7379 45%,#3a3d44 75%,#1b1f27 100%)}
.hero-copy{position:absolute;left:356px;top:52px;width:292px;color:var(--white)}
.hero-copy h1{font-size:23px;font-weight:700;line-height:31px}
.hero-copy p{font-size:7.6px;line-height:12px;margin-top:10px;color:#e8e8e8}
.hero-dots{position:absolute;right:50px;top:219px;display:flex;gap:9px}
.hero-dots i{width:9px;height:9px;border-radius:50%;background:var(--teal-light);display:block}
.hero-dots i.active{background:none;border:1.5px solid var(--white);position:relative}
.hero-dots i.active::after{content:"";position:absolute;left:1.5px;top:1.5px;width:3px;height:3px;border-radius:50%;background:var(--white)}

/* product categories */
.section-title{position:absolute;left:0;width:698px;text-align:center;font-size:19px;font-weight:700;color:var(--title)}
.categories{position:absolute;top:370px;left:50px;display:flex;gap:15px}
.category{position:relative;width:138px;height:127px;border:1px solid #c8c8c8;box-shadow:0 1px 3px rgba(0,0,0,.25);background:#fff}
.category-photo{position:absolute;left:0;top:0;width:136px;height:111px;background:linear-gradient(135deg,#e4e4e4,#8e8f92 55%,#d0d0d0)}
.category-label{position:absolute;left:0;bottom:0;width:136px;height:14px;background:var(--nav);color:var(--white);font-size:8px;font-weight:700;text-align:center;line-height:14px}
.category.featured .category-photo{left:4px;top:4px;width:128px;height:117px;background:var(--teal)}
.featured-text{position:absolute;left:0;top:44px;width:136px;text-align:center;color:var(--white)}
.featured-text strong{display:block;font-size:8.5px;font-weight:700}
.featured-text span{display:inline-block;margin-top:5px;border:1px solid var(--white);font-size:8px;font-weight:600;padding:1px 11px}

/* features */
.features-band{position:absolute;top:524px;left:0;width:698px;height:218px;background:var(--band)}
.features-title{position:absolute;left:49px;top:22px;font-size:19px;font-weight:700;color:var(--title)}
.feature{position:absolute;width:150px}
.feature svg{position:absolute;left:0;top:0;width:24px;height:24px}
.feature h3{position:absolute;left:36px;top:4px;font-size:8.5px;font-weight:700;color:#555;letter-spacing:.2px;white-space:nowrap}
.feature p{position:absolute;left:36px;top:22px;font-size:7.6px;line-height:12px;color:var(--muted);width:112px}
.video{position:absolute;left:361px;top:28px;width:287px;height:161px;background:linear-gradient(120deg,#3a3326 0%,#8c7a55 35%,#4a4c50 65%,#2a2c30 100%)}
.video-bar{position:absolute;left:0;top:0;width:287px;height:18px;background:rgba(0,0,0,.85);color:var(--white);font-size:9px;line-height:18px;padding-left:7px}
.video-play{position:absolute;left:129px;top:66px;width:30px;height:30px;border-radius:50%;background:rgba(255,255,255,.9)}
.video-play::after{content:"";position:absolute;left:12px;top:9px;border-left:9px solid var(--dark);border-top:6px solid transparent;border-bottom:6px solid transparent}
.video-caption{position:absolute;left:8px;top:126px;font-size:6.5px;font-weight:700;color:var(--white)}
.video-controls{position:absolute;left:0;bottom:0;width:287px;height:18px;background:rgba(0,0,0,.55);color:#ddd;font-size:6px;line-height:18px;padding-left:40px}
.video-controls::before{content:"";position:absolute;left:8px;right:8px;top:1px;height:2px;background:#777}

/* news */
.news{position:absolute;top:813px;left:50px;display:flex;gap:16px}
.news-card{width:189px}
.news-photo{position:relative;width:189px;height:179px;border:1px solid #bbb;box-shadow:0 1px 3px rgba(0,0,0,.25)}
.news-photo .fill{position:absolute;inset:0}
.news-date{position:absolute;left:0;bottom:0;width:86px;height:22px;background:var(--teal);color:var(--white);font-size:9px;line-height:22px;text-align:center}
.news-card h3{margin-top:22px;font-size:11.5px;font-weight:400;line-height:15px;color:#222;letter-spacing:-.2px}
.news-card p{margin-top:3px;font-size:7.6px;line-height:12px;color:var(--muted)}

/* footer */
.site-footer{position:absolute;top:1093px;left:0;width:698px;height:86px;border-top:1px solid #ddd}
.footer-col h4{font-size:9px;font-weight:400;color:#333}
.footer-contact{position:absolute;left:50px;top:10px}
.footer-contact li{list-style:none;font-size:7.6px;color:#333;display:flex;align-items:center;gap:6px;margin-top:9px}
.footer-contact svg{width:7px;height:7px;fill:#333}
.footer-about{position:absolute;left:281px;top:10px;width:170px}
.footer-about p{font-size:7.6px;line-height:12px;color:#333;margin-top:8px}
.footer-about a{display:block;font-size:7.6px;color:var(--teal);margin-top:7px;text-decoration:none;font-weight:600}
.footer-brand{position:absolute;right:50px;top:12px;display:flex;align-items:center;gap:5px}
.footer-social{position:absolute;left:503px;top:52px;font-size:11px;font-weight:600;color:#222}
.legal-bar{position:absolute;top:1179px;left:0;width:698px;height:21px;background:#000;color:var(--white);font-size:7.6px;text-align:center;line-height:21px;font-weight:600}
</style>
</head>
<body>

<header class="site-header">
  <div class="brand"><span class="brand-dot"></span><span class="brand-name">KRV Holdfast Group</span></div>
  <div class="header-contacts">
    <span><svg viewBox="0 0 10 10"><path d="M5 1L0.5 5H2v4h2.2V6.5h1.6V9H8V5h1.5z"/></svg>1870 Kestrel Ln | Marlow Falls, WI 53990</span>
    <span><svg viewBox="0 0 10 10"><path d="M2 0.5l2 2-1 1.3c.6 1.3 1.6 2.3 2.9 2.9L7.2 5.7l2.3 2-1.2 1.8C4.5 9.5.5 5.5.5 1.7z"/></svg>920-555-0147</span>
    <span><svg viewBox="0 0 10 10"><path d="M0.5 2h9v6h-9z M0.8 2.3L5 5.5l4.2-3.2" stroke="#fff" stroke-width=".6"/></svg>sales@holdfastgroup.example</span>
  </div>
</header>

<nav class="main-nav">
  <a>Home</a><a>Products</a><a>Capabilities</a><a>Engineering</a><a>Quality</a><a>About Us</a><a>Contact/Quote Request</a>
</nav>

<section class="hero">
  <div class="hero-photo" role="img" aria-label="Close-up photograph of large hex bolts and nuts on a steel flange"></div>
  <div class="hero-copy">
    <h1>Simple Ideas Help the Industry Take Off...</h1>
    <p>Lorem Ipsum is simply dummy text of the printing and typesetting industry. Lorem Ipsum has been the industry's standard dummy text ever since the 1500s, when an unknown printer took a galley of type and scrambled it to make a type specimen book.</p>
  </div>
  <div class="hero-dots"><i class="active"></i><i></i><i></i><i></i></div>
</section>

<h2 class="section-title" style="top:321px">Product Categories</h2>
<div class="categories">
  <div class="category"><div class="category-photo" role="img" aria-label="Photograph of assorted hitch pins and clevis pins"></div><div class="category-label">Lock Washers</div></div>
  <div class="category"><div class="category-photo" role="img" aria-label="Photograph of assorted screws and bolts"></div><div class="category-label">Pins</div></div>
  <div class="category"><div class="category-photo" role="img" aria-label="Photograph of stamped washers and lock washers"></div><div class="category-label">Stampings</div></div>
  <div class="category featured"><div class="category-photo" role="img" aria-label="Photograph of split lock washers under a teal overlay"></div>
    <div class="featured-text"><strong>Threaded</strong><span>View More</span></div></div>
</div>

<section class="features-band">
  <h2 class="features-title">Features</h2>
  <div class="feature" style="left:50px;top:66px">
    <svg viewBox="0 0 24 24" fill="none" stroke="#17a58a" stroke-width="1.8"><circle cx="12" cy="12" r="2.5" fill="#17a58a"/><path d="M8 8a5.5 5.5 0 0 0 0 8M16 8a5.5 5.5 0 0 1 0 8M5 5a9.5 9.5 0 0 0 0 14M19 5a9.5 9.5 0 0 1 0 14"/></svg>
    <h3>ANTI-VIBRATION</h3><p>Lorem ipsum dolor sit amet, ea doming epicuri iudicabit</p>
  </div>
  <div class="feature" style="left:202px;top:66px">
    <svg viewBox="0 0 24 24"><circle cx="12" cy="12" r="8" fill="none" stroke="#17a58a" stroke-width="4" stroke-dasharray="3 2.3"/><circle cx="12" cy="12" r="6" fill="#17a58a"/><circle cx="12" cy="12" r="2.5" fill="#ececec"/></svg>
    <h3>ENGINEERED</h3><p>Lorem ipsum dolor sit amet, ea doming epicuri iudicabit</p>
  </div>
  <div class="feature" style="left:50px;top:141px">
    <svg viewBox="0 0 24 24" fill="#17a58a"><circle cx="13" cy="7" r="5"/><circle cx="13" cy="7" r="2" fill="#ececec"/><path d="M1 16h5l4 2h6l5-3 1 2-6 4H8l-4-1H1z"/></svg>
    <h3>SERVICE ABILITY</h3><p>Lorem ipsum dolor sit amet, ea doming epicuri iudicabit</p>
  </div>
  <div class="feature" style="left:202px;top:141px">
    <svg viewBox="0 0 24 24" fill="#17a58a"><ellipse cx="8" cy="19" rx="6" ry="2.2"/><ellipse cx="8" cy="15" rx="6" ry="2.2"/><ellipse cx="8" cy="11" rx="6" ry="2.2"/><ellipse cx="17" cy="16" rx="6" ry="2.2"/><ellipse cx="17" cy="12" rx="6" ry="2.2"/><ellipse cx="17" cy="8" rx="6" ry="2.2"/><ellipse cx="17" cy="4.5" rx="6" ry="2.2"/></svg>
    <h3>COST-SAVINGS</h3><p>Lorem ipsum dolor sit amet, ea epicuri iudicabit nam.</p>
  </div>
  <div class="video" role="img" aria-label="Video still of a close-up of meshing metal gears">
    <div class="video-bar">Lorem Ipsum is simply dummy text</div>
    <div class="video-play"></div>
    <div class="video-caption">Holdfast Spiral Video</div>
    <div class="video-controls">0:00/6:54</div>
  </div>
</section>

<h2 class="section-title" style="top:764px">News &amp; Events</h2>
<div class="news">
  <article class="news-card">
    <div class="news-photo"><div class="fill" role="img" aria-label="Photograph of an engine transmission assembly" style="background:linear-gradient(135deg,#2a2a2c,#8a8b8e 50%,#3a3a3d)"></div><div class="news-date">20 May 2020</div></div>
    <h3>KRV Integrates Leading Midwest Fastener Divisions Carrow Hill, IL</h3>
    <p>Ipsum dolor sit amet, consectetur adipiscing elit, sed do eiusmod tempor incididunt ut labore et</p>
  </article>
  <article class="news-card">
    <div class="news-photo"><div class="fill" role="img" aria-label="Rendered image of steel gears and a cylindrical bushing" style="background:linear-gradient(135deg,#1f2a2c,#6e8a8e 50%,#263234)"></div><div class="news-date">20 May 2020</div></div>
    <h3>KRV Integrates Leading Midwest Fastener Divisions Carrow Hill, IL</h3>
    <p>Lorem ipsum dolor sit amet, consectetur adipiscing elit, sed do eiusmod tempor incididunt</p>
  </article>
  <article class="news-card">
    <div class="news-photo"><div class="fill" role="img" aria-label="Photograph of a pile of steel hex bolts" style="background:linear-gradient(135deg,#9a9b9e,#4b4c50 50%,#b2b3b6)"></div><div class="news-date">20 May 2020</div></div>
    <h3>KRV Integrates Leading Midwest Fastener Divisions Carrow Hill, IL</h3>
    <p>Dolor sit amet, consectetur adipiscing elit, sed do eiusmod tempor incididunt ut labore et dolore</p>
  </article>
</div>

<footer class="site-footer">
  <div class="footer-col footer-contact">
    <h4>Contact Us</h4>
    <ul>
      <li><svg viewBox="0 0 10 10"><path d="M5 1L0.5 5H2v4h2.2V6.5h1.6V9H8V5h1.5z"/></svg>1870 Kestrel Ln | Marlow Falls, WI 53990</li>
      <li><svg viewBox="0 0 10 10"><path d="M2 0.5l2 2-1 1.3c.6 1.3 1.6 2.3 2.9 2.9L7.2 5.7l2.3 2-1.2 1.8C4.5 9.5.5 5.5.5 1.7z"/></svg>920-555-0147</li>
      <li><svg viewBox="0 0 10 10"><path d="M0.5 2h9v6h-9z"/></svg>sales@holdfastgroup.example</li>
    </ul>
  </div>
  <div class="footer-col footer-about">
    <h4>About Us</h4>
    <p>Lorem ipsum dolor sit amet, ea doming epicuri iu abit nam.</p>
    <a>Read More</a>
  </div>
  <div class="footer-brand"><span class="brand-dot"></span><span class="brand-name">KRV Holdfast Group</span></div>
  <div class="footer-social">Profilenet</div>
</footer>
<div class="legal-bar">Terms &amp; Conditions | © 2017 KRV Holdfast Group</div>

</body>
</html>
```